Business card for acupunctist in Melbourne. Specialises in Fertility, pre and post natal care, pain

I am looking for a business card which is going to catch people eyes. Two sided, one side in a muted colour (keeping it feminine) (pink or yellow???)maybe with a little simple logo or picture, the other side I was thinking white with 3 colours (pink grey and yellow... Had these in mind.
Info on the card
Maren Quillby Acupuncture

Dr Maren Quillby (TCM Acupuncture)
Acupuncture for balancing body and mind.
Verdant Osprey Clinic
14 Corran Lane, Eastwood 3071.
96274158
0438215074
Marentcm@quorvenmail.com

Some other little logo/ designs I have liked are as follows:
http://www.tessrolfeclinic.com/rates-and-insurance/
http://www.corabethwinslow.com/
http://www.zd-needlework.co.uk/

Target Market(s)

professional women, people in pain, active people, people seeking a healthy lifefstyle.

Industry/Entity Type

Business

Font styles to use
Serif
Sans Serif

Colors
eea4c8
fde08a
aaaaaa

Requirements
Must have
• Must be eye catching, but not too loud and busy. Subltle is good. Simple is also good. The logo could be something that represents growth and health and nurturing. Again not too elaborate, very simple.
Thankyou
Should not have
• Electric colours, crazy fonts, Pictures of yin and yang, candles, or bodies.

```html
<!DOCTYPE html>
<html lang="en">
<head>
<meta charset="utf-8">
<title>Maren Quillby Acupuncture – Business Card</title>
<link rel="stylesheet" href="https://fonts.googleapis.com/css2?family=Quicksand:wght@400;500&family=Open+Sans:wght@400;600&display=swap">
<style>
  :root {
    --backdrop: #a8a8a8;
    --blush: #eea4c8;
    --blush-deep: #e68fba;
    --blush-card: #eda2c7;
    --butter: #fde08a;
    --stone: #aaaaaa;
    --ink: #555555;
    --paper: #ffffff;
  }
  * { box-sizing: border-box; margin: 0; padding: 0; }
  html, body {
    width: 1200px; height: 900px; overflow: hidden;
    background: var(--backdrop);
  }
  .canvas {
    width: 1200px; height: 900px;
    display: flex; align-items: center; justify-content: center; gap: 40px;
  }
  .card {
    position: relative;
    width: 540px; height: 330px;
    border-radius: 22px;
    overflow: hidden;
  }
  .card__frame {
    position: absolute; inset: 12px;
    border-radius: 16px;
    border: 8px solid var(--blush);
  }
  .card--front { background: var(--paper); }
  .card--back { background: var(--blush-card); }
  .card--back .card__frame { border-color: var(--paper); }

  .brand {
    display: flex; align-items: flex-start; gap: 10px;
    font-family: "Quicksand", sans-serif; font-weight: 400;
    color: var(--blush-deep);
  }
  .brand__dot {
    flex: none; width: 34px; height: 34px; border-radius: 50%;
    background: var(--butter);
  }
  .brand__name { line-height: 1; }
  .brand__line1 { display: block; font-size: 40px; }
  .brand__line2 { display: block; font-size: 16px; letter-spacing: 6px; margin-top: 6px; }

  .card--front .brand { position: absolute; left: 34px; top: 44px; }
  .card--back .brand {
    position: absolute; left: 130px; top: 112px; color: var(--paper);
  }
  .card--back .brand__dot { background: var(--paper); }

  .halo {
    position: absolute; border-radius: 50%;
    background: var(--butter); opacity: 0.35;
  }
  .card--front .halo { width: 170px; height: 170px; right: 28px; bottom: 24px; }
  .card--back .halo {
    width: 200px; height: 200px; left: -10px; top: -10px;
    background: var(--paper); opacity: 0.22;
  }

  .details {
    position: absolute; left: 40px; top: 166px;
    font-family: "Open Sans", sans-serif; color: var(--ink);
  }
  .details__title { font-size: 13px; font-weight: 600; color: var(--blush-deep); }
  .details__title small { font-size: 11px; font-weight: 400; }
  .details__tagline, .details__clinic { font-size: 10px; line-height: 1.35; }
  .contact { list-style: none; margin-top: 22px; font-size: 12px; line-height: 1.45; }
  .contact li { display: flex; align-items: flex-start; gap: 7px; }
  .contact svg { flex: none; width: 11px; height: 11px; margin-top: 3px; fill: var(--blush-deep); }
  .contact .contact__extra { padding-left: 18px; }
</style>
</head>
<body>
<main class="canvas">
  <section class="card card--front" aria-label="Card front">
    <div class="card__frame"></div>
    <div class="halo" aria-hidden="true"></div>
    <div class="brand">
      <span class="brand__dot"></span>
      <span class="brand__name">
        <span class="brand__line1">Maren Quillby</span>
        <span class="brand__line2">ACUPUNCTURE</span>
      </span>
    </div>
    <div class="details">
      <p class="details__title">Dr Maren Quillby <small>(TCM Acupuncture)</small></p>
      <p class="details__tagline">Acupuncture for balancing body and mind.</p>
      <p class="details__clinic">Verdant Osprey Clinic</p>
      <ul class="contact">
        <li><svg viewBox="0 0 24 24"><path d="M6.6 10.8a15.1 15.1 0 0 0 6.6 6.6l2.2-2.2c.3-.3.7-.4 1-.2 1.1.4 2.3.6 3.6.6.6 0 1 .4 1 1V20c0 .6-.4 1-1 1A17 17 0 0 1 3 4c0-.6.4-1 1-1h3.5c.6 0 1 .4 1 1 0 1.3.2 2.5.6 3.6.1.3 0 .7-.2 1z"/></svg>0438215074</li>
        <li><svg viewBox="0 0 24 24"><path d="M2 5h20v14H2zm2 2v.5l8 5 8-5V7z"/></svg>Marentcm@quorvenmail.com</li>
        <li><svg viewBox="0 0 24 24"><path d="M12 3l10 9h-3v9h-5v-6h-4v6H5v-9H2z"/></svg>14 Corran Lane, Eastwood 3071.</li>
        <li class="contact__extra">96274158</li>
      </ul>
    </div>
  </section>

  <section class="card card--back" aria-label="Card back">
    <div class="card__frame"></div>
    <div class="halo" aria-hidden="true"></div>
    <div class="brand">
      <span class="brand__dot"></span>
      <span class="brand__name">
        <span class="brand__line1">Maren Quillby</span>
        <span class="brand__line2">ACUPUNCTURE</span>
      </span>
    </div>
  </section>
</main>
</body>
</html>
```